Lowen Academy

I need different posters for a high school that displays positive messaging and the school's core values.
Want the design to look sleek for high school aged children

1. Poster #1
CORE VALUES:
• RESPECT
• RESPONSIBILITY
• LEADERSHIP
• PRIDE
• COMMUNITY

2. Acronym posters for the school
Empathy
Zeal
Respect
Aspire

3. additional acronym poster
Encourage
Zenith
Relationships
Accountability

```html
<!DOCTYPE html>
<html lang="en">
<head>
<meta charset="utf-8">
<title>Lowen Academy – Poster Series</title>
<link href="https://fonts.googleapis.com/css2?family=Oswald:wght@600&family=Montserrat:wght@700;800&display=swap" rel="stylesheet">
<style>
:root{
  --navy-top:#2e2c82;
  --navy-mid:#23216b;
  --navy-deep:#14133f;
  --ink:#1b1a4f;
  --white:#ffffff;
  --orange:#fdaa22;
  --cyan:#12c6f2;
  --green:#84c13c;
  --purple:#b04fe0;
  --red-orange:#ff6a1a;
  --ring-grey:#c9c9cf;
  --page:#ffffff;
}
*{margin:0;padding:0;box-sizing:border-box}
html,body{width:1200px;height:2602px;overflow:hidden;background:var(--page)}
.sheet{position:relative;width:1200px;height:2602px}
.poster{
  position:absolute;width:484px;height:626px;overflow:hidden;
  background:radial-gradient(ellipse at 50% 35%,var(--navy-top) 0%,var(--navy-mid) 55%,var(--navy-deep) 100%);
  box-shadow:0 6px 16px rgba(0,0,0,.35);
  font-family:"Montserrat",sans-serif;
}
.poster--hero{left:325px;top:143px;transform:scale(1.116);transform-origin:0 0}
.poster--values{left:80px;top:1100px}
.poster--acronym{left:624px;top:1100px}
.poster--extra{left:352px;top:1810px}
.abs{position:absolute}
.title-condensed{font-family:"Oswald",sans-serif;font-weight:600;color:var(--white);line-height:1;letter-spacing:-1px}
.title-bold{font-family:"Montserrat",sans-serif;font-weight:800;line-height:1}
.values-title{position:absolute;left:85px;top:30px;width:310px;display:flex;align-items:flex-end;justify-content:space-between}
.values-title__our{font-size:84px;line-height:.9}
.values-title__stack{display:flex;flex-direction:column;align-items:flex-start}
.values-title__core{font-size:46px;color:var(--orange)}
.values-title__values{font-size:36px;color:var(--cyan);margin-top:2px}
.rule{position:absolute;height:2px;background:var(--white)}
.brand{position:absolute;left:0;right:0;text-align:center;color:var(--white);font-family:"Montserrat",sans-serif;font-weight:700;font-size:17px;letter-spacing:2px}
.art{position:absolute;border-radius:8px}
.value-pill{position:absolute;height:32px;border-radius:0 8px 8px 0;color:var(--ink);font-weight:800;font-size:12px;line-height:32px;padding-left:28px;white-space:nowrap}
.value-badge{position:absolute;width:44px;height:44px;border-radius:50%;background:var(--white);border:3px solid #d7d7dd}
.value-badge::after{content:"";position:absolute;left:11px;top:11px;width:16px;height:16px;border-radius:50%;background:var(--ink)}
.step-word{position:absolute;color:var(--white);font-weight:800;font-size:27px;line-height:1}
.band{position:absolute;height:68px;color:var(--white);font-weight:800;font-size:24px;line-height:68px;text-align:center;white-space:nowrap}
.band-icon{position:absolute;width:32px;height:32px;border-radius:3px}
</style>
</head>
<body>
<div class="sheet">

  <!-- Core values poster (featured) -->
  <section class="poster poster--hero" aria-label="Our core values poster">
    <div class="values-title">
      <div class="title-condensed values-title__our">OUR</div>
      <div class="values-title__stack">
        <div class="title-bold values-title__core">CORE</div>
        <div class="title-bold values-title__values">VALUES</div>
      </div>
    </div>
    <div class="rule" style="left:85px;top:120px;width:310px"></div>
    <svg class="abs" style="left:0;top:0" width="484" height="626" viewBox="0 0 484 626">
      <circle cx="242" cy="272" r="133" fill="var(--white)" stroke="var(--ring-grey)" stroke-width="8"/>
      <circle cx="244" cy="262" r="72" fill="var(--ink)"/>
      <g stroke="var(--ink)" stroke-width="3">
        <line x1="175" y1="165" x2="198" y2="205"/><line x1="309" y1="165" x2="286" y2="205"/>
        <line x1="112" y1="276" x2="160" y2="276"/><line x1="324" y1="276" x2="372" y2="276"/>
      </g>
      <circle cx="242" cy="180" r="11" fill="var(--purple)"/>
      <circle cx="150" cy="232" r="11" fill="var(--cyan)"/>
      <circle cx="334" cy="232" r="11" fill="var(--orange)"/>
      <circle cx="150" cy="306" r="11" fill="var(--green)"/>
      <circle cx="334" cy="306" r="11" fill="var(--red-orange)"/>
      <text x="244" y="240" text-anchor="middle" fill="var(--white)" font-family="Montserrat,sans-serif" font-weight="700" font-size="21" letter-spacing="1">LOWEN</text>
      <text x="244" y="253" text-anchor="middle" fill="var(--white)" font-family="Montserrat,sans-serif" font-weight="700" font-size="7" letter-spacing="1">ACADEMY</text>
    </svg>
    <div class="art" role="img" aria-label="Illustration of a graduation cap resting on a stack of books with a diploma scroll" style="left:160px;top:272px;width:158px;height:160px;background:linear-gradient(160deg,#2a2a2a 0%,#8a3a22 40%,#2b4aa0 70%,#e9e4d4 100%);opacity:.9"></div>

    <div class="value-pill" style="left:85px;top:453px;width:152px;background:var(--green)">RESPECT</div>
    <div class="value-badge" style="left:56px;top:447px"></div>
    <div class="value-pill" style="left:276px;top:453px;width:156px;background:var(--cyan)">RESPONSIBILITY</div>
    <div class="value-badge" style="left:246px;top:447px"></div>
    <div class="value-pill" style="left:85px;top:506px;width:152px;background:var(--purple)">LEADERSHIP</div>
    <div class="value-badge" style="left:56px;top:500px"></div>
    <div class="value-pill" style="left:276px;top:503px;width:156px;background:var(--orange)">PRIDE</div>
    <div class="value-badge" style="left:246px;top:497px"></div>
    <div class="value-pill" style="left:182px;top:556px;width:150px;background:var(--red-orange)">COMMUNITY</div>
    <div class="value-badge" style="left:152px;top:550px"></div>
  </section>

  <!-- Core values poster -->
  <section class="poster poster--values" aria-label="Our core values poster">
    <div class="values-title">
      <div class="title-condensed values-title__our">OUR</div>
      <div class="values-title__stack">
        <div class="title-bold values-title__core">CORE</div>
        <div class="title-bold values-title__values">VALUES</div>
      </div>
    </div>
    <div class="rule" style="left:85px;top:120px;width:310px"></div>
    <svg class="abs" style="left:0;top:0" width="484" height="626" viewBox="0 0 484 626">
      <circle cx="242" cy="272" r="133" fill="var(--white)" stroke="var(--ring-grey)" stroke-width="8"/>
      <circle cx="244" cy="262" r="72" fill="var(--ink)"/>
      <g stroke="var(--ink)" stroke-width="3">
        <line x1="175" y1="165" x2="198" y2="205"/><line x1="309" y1="165" x2="286" y2="205"/>
        <line x1="112" y1="276" x2="160" y2="276"/><line x1="324" y1="276" x2="372" y2="276"/>
      </g>
      <circle cx="242" cy="180" r="11" fill="var(--purple)"/>
      <circle cx="150" cy="232" r="11" fill="var(--cyan)"/>
      <circle cx="334" cy="232" r="11" fill="var(--orange)"/>
      <circle cx="150" cy="306" r="11" fill="var(--green)"/>
      <circle cx="334" cy="306" r="11" fill="var(--red-orange)"/>
      <text x="244" y="240" text-anchor="middle" fill="var(--white)" font-family="Montserrat,sans-serif" font-weight="700" font-size="21" letter-spacing="1">LOWEN</text>
      <text x="244" y="253" text-anchor="middle" fill="var(--white)" font-family="Montserrat,sans-serif" font-weight="700" font-size="7" letter-spacing="1">ACADEMY</text>
    </svg>
    <div class="art" role="img" aria-label="Illustration of a graduation cap resting on a stack of books with a diploma scroll" style="left:160px;top:272px;width:158px;height:160px;background:linear-gradient(160deg,#2a2a2a 0%,#8a3a22 40%,#2b4aa0 70%,#e9e4d4 100%);opacity:.9"></div>

    <div class="value-pill" style="left:85px;top:453px;width:152px;background:var(--green)">RESPECT</div>
    <div class="value-badge" style="left:56px;top:447px"></div>
    <div class="value-pill" style="left:276px;top:453px;width:156px;background:var(--cyan)">RESPONSIBILITY</div>
    <div class="value-badge" style="left:246px;top:447px"></div>
    <div class="value-pill" style="left:85px;top:506px;width:152px;background:var(--purple)">LEADERSHIP</div>
    <div class="value-badge" style="left:56px;top:500px"></div>
    <div class="value-pill" style="left:276px;top:503px;width:156px;background:var(--orange)">PRIDE</div>
    <div class="value-badge" style="left:246px;top:497px"></div>
    <div class="value-pill" style="left:182px;top:556px;width:150px;background:var(--red-orange)">COMMUNITY</div>
    <div class="value-badge" style="left:152px;top:550px"></div>
  </section>

  <!-- Acronym poster -->
  <section class="poster poster--acronym" aria-label="Acronym poster">
    <div class="abs title-condensed" style="left:0;right:0;top:26px;text-align:center;font-size:72px">ACRONYM</div>
    <div class="rule" style="left:118px;top:102px;width:250px"></div>
    <div class="art" role="img" aria-label="Illustration of standing books, a rolled scroll and a graduation cap" style="left:152px;top:116px;width:180px;height:126px;background:linear-gradient(120deg,#7bbf1e 0%,#2a9a8a 35%,#1a1a1a 65%,#e8d6b0 100%);opacity:.9"></div>

    <svg class="abs" style="left:0;top:0" width="484" height="626" viewBox="0 0 484 626" font-family="Montserrat,sans-serif">
      <rect x="110" y="252" width="262" height="64" fill="#1e1c5e"/>
      <polyline points="128,252 98,284 128,316" fill="none" stroke="var(--green)" stroke-width="5"/>
      <line x1="128" y1="252" x2="372" y2="252" stroke="var(--green)" stroke-width="2"/>
      <text x="148" y="270" fill="#9a98c8" font-size="8" font-weight="700" letter-spacing="2">STEP</text>
      <text x="146" y="305" fill="var(--green)" font-family="Oswald,sans-serif" font-size="36" font-weight="600">01</text>
      <line x1="182" y1="262" x2="182" y2="306" stroke="#4b49a0" stroke-width="1"/>
      <circle cx="62" cy="285" r="16" fill="var(--green)"/>

      <rect x="112" y="322" width="262" height="64" fill="#1e1c5e"/>
      <polyline points="362,322 390,354 362,386" fill="none" stroke="var(--cyan)" stroke-width="5"/>
      <line x1="112" y1="322" x2="362" y2="322" stroke="var(--cyan)" stroke-width="2"/>
      <text x="322" y="340" fill="#9a98c8" font-size="8" font-weight="700" letter-spacing="2">STEP</text>
      <text x="318" y="375" fill="var(--cyan)" font-family="Oswald,sans-serif" font-size="36" font-weight="600">02</text>
      <line x1="306" y1="332" x2="306" y2="376" stroke="#4b49a0" stroke-width="1"/>
      <circle cx="420" cy="350" r="15" fill="var(--cyan)"/>

      <rect x="110" y="392" width="262" height="64" fill="#1e1c5e"/>
      <polyline points="128,392 98,424 128,456" fill="none" stroke="var(--purple)" stroke-width="5"/>
      <line x1="128" y1="392" x2="372" y2="392" stroke="var(--purple)" stroke-width="2"/>
      <text x="148" y="410" fill="#9a98c8" font-size="8" font-weight="700" letter-spacing="2">STEP</text>
      <text x="146" y="445" fill="var(--purple)" font-family="Oswald,sans-serif" font-size="36" font-weight="600">03</text>
      <line x1="182" y1="402" x2="182" y2="446" stroke="#4b49a0" stroke-width="1"/>
      <circle cx="62" cy="427" r="16" fill="var(--purple)"/>

      <rect x="112" y="462" width="262" height="64" fill="#1e1c5e"/>
      <polyline points="362,462 390,494 362,526" fill="none" stroke="var(--orange)" stroke-width="5"/>
      <line x1="112" y1="526" x2="362" y2="526" stroke="var(--orange)" stroke-width="2"/>
      <text x="322" y="480" fill="#9a98c8" font-size="8" font-weight="700" letter-spacing="2">STEP</text>
      <text x="318" y="515" fill="var(--orange)" font-family="Oswald,sans-serif" font-size="36" font-weight="600">04</text>
      <line x1="306" y1="472" x2="306" y2="516" stroke="#4b49a0" stroke-width="1"/>
      <circle cx="422" cy="490" r="14" fill="var(--orange)"/>
    </svg>
    <div class="step-word" style="left:191px;top:273px">EMPATHY</div>
    <div class="step-word" style="right:192px;top:343px">ZEAL</div>
    <div class="step-word" style="left:191px;top:413px">RESPECT</div>
    <div class="step-word" style="right:192px;top:483px">ASPIRE</div>
    <div class="brand" style="top:560px">LOWEN ACADEMY</div>
  </section>

  <!-- Additional acronym poster -->
  <section class="poster poster--extra" aria-label="Additional acronym poster">
    <div class="abs title-condensed" style="left:0;right:0;top:46px;text-align:center;font-size:74px">ADDITIONAL</div>
    <div class="abs title-condensed" style="left:0;right:0;top:114px;text-align:center;font-size:74px;color:var(--orange)">ACRONYM</div>
    <div class="rule" style="left:88px;top:193px;width:307px"></div>

    <div class="band" style="left:52px;top:228px;width:336px;padding-left:40px;background:var(--green);clip-path:polygon(3% 0,97% 0,100% 100%,0 100%)">ENCOURAGE</div>
    <div class="band-icon" style="left:80px;top:246px;background:var(--cyan)"></div>
    <div class="band" style="left:95px;top:296px;width:337px;padding-right:40px;background:var(--cyan);clip-path:polygon(3% 0,100% 0,97% 100%,0 100%)">ZENITH</div>
    <div class="band-icon" style="left:370px;top:314px;background:var(--green)"></div>
    <div class="band" style="left:52px;top:364px;width:336px;padding-left:56px;background:var(--purple);clip-path:polygon(3% 0,97% 0,100% 100%,0 100%)">RELATIONSHIPS</div>
    <div class="band-icon" style="left:80px;top:382px;background:var(--orange)"></div>
    <div class="band" style="left:95px;top:432px;width:337px;padding-left:10px;padding-right:56px;background:var(--orange);clip-path:polygon(3% 0,100% 0,97% 100%,0 100%)">ACCOUNTABILITY</div>
    <div class="band-icon" style="left:380px;top:450px;background:var(--purple)"></div>

    <div class="brand" style="top:556px">LOWEN ACADEMY</div>
  </section>

</div>
</body>
</html>
```